Postcard Design Project

private loan company where loans are funded by private individual investors.
This would be a postcard advertising for additional investors.

```html
<!DOCTYPE html>
<html lang="en">
<head>
<meta charset="utf-8">
<title>Harborline Capital Lending – Investor Postcard</title>
<link href="https://fonts.googleapis.com/css2?family=Cinzel:wght@500;600&family=Lato:wght@400;700&display=swap" rel="stylesheet">
<style>
:root{
  --stage:#a9a9a9;
  --paper:#ffffff;
  --navy:#0f2340;
  --charcoal:#272727;
  --gold:#d9a621;
  --gold-text:#c8951a;
  --ink:#1d1d1d;
  --line:#9a9a9a;
  --photo-warm-a:#f1e6d7;
  --photo-warm-b:#c99d7c;
  --photo-cool-a:#dfe9f2;
  --photo-cool-b:#9db4c8;
  --photo-green-a:#cfe0c2;
  --photo-green-b:#7d9a6b;
}
*{margin:0;padding:0;box-sizing:border-box}
html,body{width:1200px;height:1200px;overflow:hidden;background:var(--stage)}
.card{position:absolute;width:696px;height:473px;background:var(--paper);overflow:hidden;font-family:"Lato",sans-serif;color:var(--ink)}
.card--front{left:119px;top:102px}
.card--back{left:400px;top:629px}
.card__art{position:absolute;left:0;top:0;width:696px;height:473px}

.brand{position:absolute;display:flex;align-items:center;gap:9px;color:var(--navy);font-family:"Cinzel",serif;font-weight:600}
.brand__dot{width:14px;height:14px;border-radius:50%;background:var(--gold);flex:none}
.brand__rule{width:1px;align-self:stretch;background:#bbb}
.brand__name{line-height:1.02}
.card--front .brand{left:45px;top:36px;height:64px;font-size:16px}
.card--front .brand__dot{width:20px;height:20px}
.card--back .brand{left:380px;top:27px;height:50px;font-size:11px;gap:7px}

.panel{position:absolute;left:0;top:118px;width:349px;height:290px;background:var(--navy)}
.quote{position:absolute;left:27px;top:139px;width:320px;font-family:"Cinzel",serif;font-weight:500;color:var(--gold);font-size:21px;line-height:26px}
.quote__author{display:block;margin-top:2px;font-size:19px;color:#f2f2f2}
.front-body{position:absolute;left:27px;top:274px;width:318px;color:#fff;font-size:11.8px;line-height:14.9px;text-align:justify}

.site{position:absolute;left:27px;top:423px;display:flex;align-items:center;gap:9px;font-size:18px;letter-spacing:1px;color:var(--ink)}
.site svg{width:17px;height:17px}
.card--back .site{left:29px;top:424px;font-size:17px}

.about__title{position:absolute;left:28px;top:23px;font-family:"Cinzel",serif;font-weight:600;font-size:24px;color:var(--navy);padding-bottom:2px;border-bottom:1.5px solid var(--navy)}
.about__text{position:absolute;left:28px;top:63px;width:300px;font-size:11.8px;line-height:15px}
.about__text a{color:var(--gold-text);text-decoration:none}
.about__phone{color:var(--gold-text);font-weight:700}
.points{position:absolute;left:28px;top:136px;width:270px;list-style:none;font-size:11.8px;line-height:15px}
.points li{position:relative;padding-left:13px;margin-bottom:8px}
.points li::before{content:"";position:absolute;left:1px;top:6px;width:4px;height:4px;border-radius:50%;background:var(--ink)}

.legal{position:absolute;left:0;top:344px;width:348px;height:73px;background:var(--charcoal);color:#eee;font-size:8.8px;line-height:11.2px;padding:8px 10px 0 28px}
.legal em{font-style:normal;color:var(--gold)}

.stamp{position:absolute;left:618px;top:27px;width:50px;height:60px;background:#e3e3e3}
.address-line{position:absolute;left:526px;width:140px;height:1px;background:#333}
</style>
</head>
<body>

<section class="card card--front" aria-label="Postcard front">
  <svg class="card__art" viewBox="0 0 696 473" aria-hidden="false">
    <defs>
      <linearGradient id="coupleTone" x1="0" y1="0" x2="1" y2="1">
        <stop offset="0" stop-color="#e9eef3"/>
        <stop offset="0.45" stop-color="var(--photo-warm-a)"/>
        <stop offset="1" stop-color="var(--photo-warm-b)"/>
      </linearGradient>
      <linearGradient id="deskTone" x1="0" y1="0" x2="1" y2="1">
        <stop offset="0" stop-color="var(--photo-cool-a)"/>
        <stop offset="1" stop-color="var(--photo-cool-b)"/>
      </linearGradient>
      <linearGradient id="houseTone" x1="0" y1="0" x2="0" y2="1">
        <stop offset="0" stop-color="#cfe2f2"/>
        <stop offset="0.55" stop-color="#d8d2c6"/>
        <stop offset="1" stop-color="var(--photo-green-b)"/>
      </linearGradient>
    </defs>
    <path role="img" aria-label="Photo of a smiling couple, the woman hugging the man from behind" d="M457,0 C360,130 360,360 477,473 L696,473 L696,0 Z" fill="url(#coupleTone)"/>
    <path d="M405,0 C300,150 320,360 465,473 L477,473 C360,360 360,130 457,0 Z" fill="var(--charcoal)"/>
    <circle cx="387" cy="199" r="86" fill="var(--gold)"/>
    <circle role="img" aria-label="Photo of hands working on financial charts with a calculator" cx="387" cy="199" r="81" fill="url(#deskTone)"/>
    <circle cx="411" cy="326" r="61" fill="var(--gold)"/>
    <circle role="img" aria-label="Photo of a two-storey family house with a front lawn" cx="411" cy="326" r="56" fill="url(#houseTone)"/>
  </svg>

  <div class="brand">
    <span class="brand__dot"></span>
    <span class="brand__rule"></span>
    <span class="brand__name">Harborline Capital<br>Lending, Inc.</span>
  </div>

  <div class="panel"></div>
  <p class="quote">He who earns and does not invest will have to work for the rest of his life.
    <span class="quote__author">- Arthur Bellamy</span></p>
  <p class="front-body">As an experienced or recent California trust deed investor I would like to invite you to join our email list to receive our trust deed investment Executive Summaries. These one-page summaries are emailed when newly originated trust deed investments are ready for review and funding. Harborline Capital Lending, Inc. has been originating privately funded or “hard money” loans in California since 2001.</p>

  <div class="site">
    <svg viewBox="0 0 20 20" fill="none" stroke="currentColor" stroke-width="1.8"><circle cx="10" cy="10" r="8"/><ellipse cx="10" cy="10" rx="3.5" ry="8"/><path d="M2 10h16M3.5 6h13M3.5 14h13"/></svg>
    <span>www.harborlineloans.info</span>
  </div>
</section>

<section class="card card--back" aria-label="Postcard back">
  <svg class="card__art" viewBox="0 0 696 473">
    <defs>
      <linearGradient id="officeTone" x1="0" y1="0" x2="1" y2="1">
        <stop offset="0" stop-color="#eef1f4"/>
        <stop offset="1" stop-color="#c9a88e"/>
      </linearGradient>
      <linearGradient id="readerTone" x1="0" y1="0" x2="1" y2="1">
        <stop offset="0" stop-color="#f1ece4"/>
        <stop offset="1" stop-color="#b49276"/>
      </linearGradient>
    </defs>
    <path d="M270,0 C345,60 355,270 258,473" fill="none" stroke="#bdbdbd" stroke-width="5"/>
    <path d="M288,0 L360,0 C400,60 420,300 288,473 L272,473 C370,300 360,60 288,0 Z" fill="var(--navy)"/>
    <circle cx="388" cy="183" r="87" fill="var(--gold)"/>
    <circle role="img" aria-label="Photo of business colleagues pointing at a growth chart on a whiteboard" cx="388" cy="183" r="81" fill="url(#officeTone)"/>
    <circle cx="374" cy="295" r="63" fill="var(--gold)"/>
    <circle role="img" aria-label="Photo of a woman reading a tablet at a desk" cx="374" cy="295" r="57" fill="url(#readerTone)"/>
  </svg>

  <h2 class="about__title">About Us</h2>
  <p class="about__text">If the monthly income offered by well-secured trust deed investments is attractive to you, please go to our website at: <a href="#">www.harborlineloans.info</a> to subscribe to our email list and learn more about Harborline and trust deed investing. <span class="about__phone">Our telephone number is 1-800-555-0147.</span></p>
  <ul class="points">
    <li>Complete investor due diligence package.</li>
    <li>Currently originating non-owner occupied residential loans (business purpose).</li>
    <li>Loan documents including note and deed of trust show your name and vesting.</li>
    <li>Fund directly to the insuring title company.</li>
    <li>Utilizing leading industry loan and lender document packages.</li>
    <li>Typical terms are for 3-7 years.</li>
    <li>Both purchase and refinance loans</li>
  </ul>

  <div class="legal">Harborline Capital Lending, Inc. 1250 Orchard Way, Suite 210 Riverside CA 92501 <em>Call (800) 555-0147</em> CA Department of Real Estate – Real Estate Broker <em>License # 00000000 NMLS # 000001</em><br>Daniel Whitmore CA Department of Real Estate – Real Estate Broker<br><em>License # 00000001 NMLS # 000002</em></div>

  <div class="site">
    <svg viewBox="0 0 20 20" fill="none" stroke="currentColor" stroke-width="1.8"><circle cx="10" cy="10" r="8"/><ellipse cx="10" cy="10" rx="3.5" ry="8"/><path d="M2 10h16M3.5 6h13M3.5 14h13"/></svg>
    <span>www.harborlineloans.info</span>
  </div>

  <div class="brand">
    <span class="brand__dot"></span>
    <span class="brand__rule"></span>
    <span class="brand__name">Harborline Capital<br>Lending, Inc.</span>
  </div>

  <div class="stamp"></div>
  <div class="address-line" style="top:186px"></div>
  <div class="address-line" style="top:216px"></div>
  <div class="address-line" style="top:245px"></div>
</section>

</body>
</html>
```